KTO Reception Posterboards

We need 3 posterboard designs for an upcoming reception. I will take your designs and have a local printer put them on foam poster board. I'll need the following please 1) Autos Move By Rail and 2) Safety

On the auto board, please include a big, prominent "3/4 of all autos move by rail." Some type of big, bold splash.

Please make sure the KTO logo is on the bottom right corner of each design.

As a side note, our poster boards are about 2 x 3 ft in size.

Target Market(s)

public officials

Industry/Entity Type

Printer

Requirements
Must have
• bold feel for the poster boards
Nice to have
• Include pics.

```html
<!DOCTYPE html>
<html lang="en">
<head>
<meta charset="utf-8">
<title>Safety Investment and Innovations</title>
<link href="https://fonts.googleapis.com/css2?family=Open+Sans:wght@400;600;700;800&display=swap" rel="stylesheet">
<style>
  :root{
    --navy:#0d1270;
    --ink:#333438;
    --paper:#e3e3e3;
    --teal:#4cbcbc;
    --white:#ffffff;
    --sky-top:#eef0f2;
    --sky-low:#c9ccd2;
    --steel:#2f4470;
    --rail:#2a2a2e;
  }
  *{margin:0;padding:0;box-sizing:border-box}
  html,body{width:800px;height:1200px;overflow:hidden;background:var(--paper)}
  body{font-family:"Open Sans",sans-serif;color:var(--ink);position:relative}
  .poster{position:relative;width:800px;height:1200px;background:var(--paper);overflow:hidden}
  .title{position:absolute;left:0;top:30px;width:800px;text-align:center;font-weight:800;
    font-size:60px;line-height:64px;color:var(--navy);letter-spacing:1px}
  .lead-quote{position:absolute;left:27px;top:170px;width:740px;font-size:21.5px;line-height:31px;
    text-align:justify;text-align-last:left;color:var(--ink)}
  .col-left{position:absolute;left:25px;top:313px;width:368px}
  .col-right{position:absolute;left:414px;top:306px;width:353px}
  h2{color:var(--navy);font-weight:700;white-space:nowrap}
  .section-head{font-size:25px;line-height:34px}
  .stats{list-style:none;margin-top:10px}
  .stats li{position:relative;padding-left:22px;font-size:15px;line-height:30px;white-space:nowrap}
  .stats li:first-child{font-size:16.5px}
  .stats li::before{content:"";position:absolute;left:2px;top:12px;width:7px;height:7px;border-radius:50%;background:var(--ink)}
  .training-head{margin-top:6px;font-size:23px;letter-spacing:-0.2px}
  .body-copy{font-size:14.5px;line-height:25.5px;text-align:justify;margin-top:6px}
  .ptc-head{font-size:21px;line-height:28px;letter-spacing:.3px}
  .ptc-copy{font-size:15px;line-height:20.5px;text-align:justify;margin-top:4px}
  .training-photo{position:absolute;left:22px;top:604px;width:371px;height:281px;border:5px solid var(--white);
    background:linear-gradient(160deg,#bcd4e8 0%,#3cb3b0 38%,#2a8f97 62%,#3d3c45 100%)}
  .chart-card{position:absolute;left:415px;top:529px;width:352px;height:227px;border:4px solid var(--white);background:var(--paper)}
  .chart-title{position:absolute;left:0;top:10px;width:100%;text-align:center;font-weight:700;font-size:13.5px;line-height:22px;color:var(--navy)}
  .chart-sub{position:absolute;left:0;top:55px;width:100%;text-align:center;font-weight:600;font-size:8.5px;color:#222}
  .chart-svg{position:absolute;left:0;top:0}
  .chart-label{position:absolute;top:200px;font-weight:700;font-size:11px;color:#222;white-space:nowrap}
  .hazmat{position:absolute;left:415px;top:772px;width:352px;font-size:14.5px;line-height:24px;text-align:justify}
  .hazmat strong{font-size:20px;color:var(--navy);font-weight:700}
  .locomotive-photo{position:absolute;left:0;top:897px;width:800px;height:303px;
    background:linear-gradient(180deg,var(--sky-top) 0%,var(--sky-low) 35%,var(--steel) 60%,#1f2a48 85%,var(--rail) 100%)}
  .brand{position:absolute;left:652px;top:912px;width:116px;color:var(--navy);font-family:"Open Sans",sans-serif;font-weight:700;text-align:center}
  .brand-mark{display:block;font-size:46px;line-height:50px;letter-spacing:1px;border-bottom:2px solid var(--navy)}
  .brand-name{display:block;font-size:12px;line-height:16px;letter-spacing:1.5px;margin-top:4px;text-transform:uppercase}
</style>
</head>
<body>
<main class="poster">
  <h1 class="title">SAFETY INVESTMENT<br>AND INNOVATIONS</h1>

  <p class="lead-quote">“Railroads’ annual investments to modernize and improve America’s freight rail network have significantly contributed to freight rail’s strong safety record. There is a direct correlation between the increase in rail network investments and enhanced safety performance.”</p>

  <section class="col-left">
    <h2 class="section-head">Since 2000:</h2>
    <ul class="stats">
      <li>The train accident rate fell 38 percent</li>
      <li>The rail employee injury rate fell 47 percent</li>
      <li>The grade crossing collision rate fell 42 percent</li>
    </ul>
    <h2 class="section-head training-head">Emergency Response Training</h2>
    <p class="body-copy">Each year, thousands of emergency responders and railroad and shipper employees receive specialized training through individual railroad efforts and industry programs.</p>
  </section>

  <div class="training-photo" role="img" aria-label="Photo of emergency responders in safety vests training beside a teal tank car"></div>

  <section class="col-right">
    <h2 class="ptc-head">POSITIVE TRAIN CONTROL (PTC)</h2>
    <p class="ptc-copy">Since 2008, freight railroads have worked closely with the federal government and passenger railroads to implement PTC — the largest and most complex safety system in the history of the railroad industry. This cutting-edge technology is designed to automatically stop a train before certain accidents occur. Emergency Response Training Each year, thousands of emergency responders and railroad.</p>
  </section>

  <figure class="chart-card">
    <svg class="chart-svg" width="344" height="219" viewBox="0 0 344 219" aria-hidden="true">
      <g transform="translate(64,132)">
        <circle r="52" fill="var(--navy)"/>
        <path d="M0,0 L0,-52 A52 52 0 0 0 -48.4,-19.1 Z" fill="var(--teal)"/>
        <circle r="17" fill="var(--white)"/>
        <rect x="-10" y="-6" width="18" height="10" fill="var(--teal)"/>
        <circle cx="-6" cy="6" r="2" fill="var(--teal)"/>
        <circle cx="4" cy="6" r="2" fill="var(--teal)"/>
        <text x="-44" y="-16" font-family="Open Sans,sans-serif" font-weight="700" font-size="14" fill="var(--white)">19%</text>
      </g>
      <text x="175" y="142" text-anchor="middle" font-family="Open Sans,sans-serif" font-weight="700" font-size="31" fill="#3a3a3a">VS.</text>
      <g transform="translate(269,132)">
        <circle r="52" fill="var(--navy)"/>
        <path d="M0,0 L0,-52 A52 52 0 0 0 -9.7,-51.1 Z" fill="var(--teal)"/>
        <circle r="17" fill="var(--white)"/>
        <rect x="-9" y="-2" width="18" height="8" fill="var(--teal)"/>
        <rect x="-7" y="-9" width="3" height="7" fill="var(--teal)"/>
        <rect x="1" y="-6" width="3" height="4" fill="var(--teal)"/>
        <text x="13" y="-34" font-family="Open Sans,sans-serif" font-weight="700" font-size="14" fill="var(--white)">3%</text>
      </g>
    </svg>
    <figcaption class="chart-title">FREIGHT RAIL INVESTS SIX TIMES MORE THAN<br>THE AVERAGE U.S. MANUFACTURER</figcaption>
    <p class="chart-sub">Capital Spending as a Percentage of Revenue</p>
    <span class="chart-label" style="left:34px">Freight Rail</span>
    <span class="chart-label" style="left:180px">Average U.S. Manufacturer</span>
  </figure>

  <p class="hazmat">Today, <strong>99.999%</strong> of all hazmat moved by rail reaches its destination without a release caused by an incident. This strong safety record is among the many reasons the federal government requires railroads to transport hazmat.”</p>

  <div class="locomotive-photo" role="img" aria-label="Photo of a blue and silver freight locomotive pulling boxcars under a pale sky"></div>

  <div class="brand">
    <span class="brand-mark">KTO</span>
    <span class="brand-name">Kestrel Transit Organization</span>
  </div>
</main>
</body>
</html>
```